The calm within me tour 2019

I need an improvement of my own design for a speaking tour on shame and mental health. The advertisement will be for social media. I would like someone to remove the background and do something creative and contemporary. My preference is just my head and shoulders.

Target Market(s)

Church pastors and leaders of mental health organisations

Industry/Entity Type

Mental Health

Requirements
Must have
• The same wording as original
• Delete background and replace with something that is simple but funky

```html
<!DOCTYPE html>
<html lang="en">
<head>
<meta charset="utf-8">
<title>The Calm Within Me Tour 2019</title>
<link rel="stylesheet" href="https://fonts.googleapis.com/css2?family=Comfortaa:wght@500&family=Montserrat:wght@800&family=Architects+Daughter&family=Quicksand:wght@500&display=swap">
<style>
  :root {
    --ink-top: #000000;
    --ink-bottom: #0d1733;
    --accent-blue: #4152d9;
    --accent-light: #5b6ff2;
    --accent-deep: #2f3cb8;
    --accent-glow: #7d8cff;
    --script-blue: #4a62ff;
    --brand-blue: #5a7cff;
    --brand-grey: #8a9aa8;
    --white: #ffffff;
    --portrait-light: #9a7a66;
    --portrait-mid: #5a4338;
    --portrait-dark: #0b0b10;
  }
  * { margin: 0; padding: 0; box-sizing: border-box; }
  html, body { width: 1200px; height: 1200px; overflow: hidden; background: #ffffff; }
  .poster {
    position: relative;
    width: 1200px;
    height: 1200px;
    overflow: hidden;
    background: linear-gradient(180deg, var(--ink-top) 0%, var(--ink-top) 45%, var(--ink-bottom) 100%);
  }
  .accent-panel {
    position: absolute;
    left: 670px;
    top: 0;
    width: 530px;
    height: 1200px;
  }
  .portrait {
    position: absolute;
    left: 600px;
    top: 140px;
    width: 600px;
    height: 1060px;
  }
  .tour-title {
    position: absolute;
    left: 0;
    top: 250px;
    width: 680px;
    text-align: center;
    color: var(--white);
    z-index: 2;
  }
  .tour-title__lead {
    display: block;
    font-family: "Comfortaa", sans-serif;
    font-weight: 500;
    font-size: 80px;
    line-height: 1;
    margin-bottom: 20px;
  }
  .tour-title__main {
    display: block;
    font-family: "Montserrat", sans-serif;
    font-weight: 800;
    font-size: 78px;
    line-height: 120px;
    letter-spacing: 1px;
  }
  .tour-title__year {
    display: block;
    margin-top: 14px;
    font-family: "Architects Daughter", cursive;
    font-style: italic;
    font-size: 80px;
    line-height: 1.2;
    letter-spacing: 8px;
    color: var(--script-blue);
  }
  .speaker-brand {
    position: absolute;
    left: 100px;
    bottom: 36px;
    display: flex;
    align-items: center;
    gap: 22px;
    z-index: 2;
  }
  .speaker-brand__mark {
    width: 48px;
    height: 48px;
    background: var(--brand-blue);
  }
  .speaker-brand__name {
    font-family: "Quicksand", sans-serif;
    font-weight: 500;
    font-size: 58px;
    color: var(--brand-grey);
  }
</style>
</head>
<body>
  <main class="poster">
    <svg class="accent-panel" viewBox="0 0 530 1200" aria-hidden="true">
      <defs>
        <linearGradient id="panel-tone" x1="0" y1="0" x2="1" y2="1">
          <stop offset="0" stop-color="var(--accent-light)"/>
          <stop offset="0.55" stop-color="var(--accent-blue)"/>
          <stop offset="1" stop-color="var(--accent-deep)"/>
        </linearGradient>
        <clipPath id="panel-clip"><rect width="530" height="1200"/></clipPath>
      </defs>
      <rect class="panel-fill" width="530" height="1200" fill="url(#panel-tone)"/>
      <g clip-path="url(#panel-clip)">
        <path class="panel-band" d="M-40 420 L530 -150 L530 20 L-40 590 Z" fill="var(--accent-deep)" opacity="0.55"/>
        <path class="panel-band" d="M-40 700 L530 130 L530 190 L-40 760 Z" fill="var(--accent-glow)" opacity="0.45"/>
        <circle class="panel-ring" cx="290" cy="450" r="300" fill="none" stroke="var(--accent-glow)" stroke-width="34" opacity="0.5"/>
        <circle class="panel-ring" cx="290" cy="450" r="220" fill="none" stroke="var(--accent-deep)" stroke-width="14" opacity="0.6"/>
        <circle class="panel-dot" cx="70" cy="110" r="26" fill="var(--white)" opacity="0.85"/>
        <circle class="panel-dot" cx="470" cy="860" r="14" fill="var(--white)" opacity="0.7"/>
      </g>
    </svg>

    <svg class="portrait" viewBox="0 0 600 1060" role="img" aria-label="Head-and-shoulders portrait of the speaker in a black v-neck t-shirt">
      <defs>
        <linearGradient id="portrait-tone" x1="0" y1="0" x2="0" y2="1">
          <stop offset="0" stop-color="var(--portrait-light)"/>
          <stop offset="0.5" stop-color="var(--portrait-mid)"/>
          <stop offset="0.72" stop-color="var(--portrait-dark)"/>
          <stop offset="1" stop-color="var(--portrait-dark)"/>
        </linearGradient>
      </defs>
      <path d="M150 330 C140 150 250 40 370 50 C500 60 560 170 545 330 C540 420 510 520 470 590
               C540 650 600 690 600 720 L600 1060 L0 1060 L0 900
               C40 790 160 720 260 690 C210 600 160 460 150 330 Z"
            fill="url(#portrait-tone)"/>
    </svg>

    <h1 class="tour-title">
      <span class="tour-title__lead">the</span>
      <span class="tour-title__main">CALM WITHIN</span>
      <span class="tour-title__main">ME</span>
      <span class="tour-title__year">TOUR 2019</span>
    </h1>

    <div class="speaker-brand">
      <span class="speaker-brand__mark"></span>
      <span class="speaker-brand__name">dan hollis</span>
    </div>
  </main>
</body>
</html>
```